Custom Framing Shop Tallpine Framing Studio

I want an eye catching graphic that will be used a s business sign on a busy road. The sign MUST communicate the type of business it is clearly to vehicles traveling at 40 mph. This is a custom picture framing business and the sign will be hanging and be approximately 32" X 48". The business name is Tallpine Framing Studio; Custom framing: by appointment and should include a whole or partial image of a picture frame as a visual que. I've included inspiration idea's, color pallets and styles that I like and a current business card for inspiration. I like the crimson font style shadowing and background colors of the attached Olans pizzeria sign. I'd prefer crimson letters. Custom Framing is the message to communicate, followed by phone number and business name. I like the idea of a shield shape with a banner since it would more eye catching, Once again the Tallpine image and name is less important than communicating what the business does. I like Crimson, grey, gold, black but am open to new ideas . I like the idea of a shield with a banner more than a rectangle, but am open to idea's

Target Market(s)

My target market is local homeowners ($700k+) who want a relationship with their framer and are willing to pay for a customized experience compared to a craft store experience. I have more female clients then men.

Industry/Entity Type

Picture Framing Art

Other font styles liked:
• Look at the attached image of a custom pizzeria sign, its kid of a custom car pinstripe font style. Script and decorative may be difficult to read while driving by but add to the elegance.

Colors

Designer to choose colors to be used in the design.

Requirements
Must have
• Clearly communicate what the business does "Custom framing" preferably with a picture frame and words
Nice to have
• incorporate a Tallpine into the graphic
Should not have
• A Tallpine image doesn't communicate what the business does to a vehicle traveling at 40 mph by the sign

```html
<!DOCTYPE html>
<html lang="en">
<head>
<meta charset="utf-8">
<title>Tallpine Framing Studio – Custom Framing Sign</title>
<link rel="stylesheet" href="https://fonts.googleapis.com/css2?family=Barlow:wght@600;700&family=Barlow+Condensed:wght@700&family=Yesteryear&display=swap">
<style>
  :root {
    --crimson: #7e1519;
    --crimson-deep: #5a0d10;
    --gold-light: #f1dfaa;
    --gold-mid: #d9b878;
    --gold-dark: #a8803c;
    --gold-band: #9c7532;
    --ink: #111111;
    --paper: #ffffff;
  }
  html, body {
    margin: 0;
    padding: 0;
    width: 1200px;
    height: 444px;
    overflow: hidden;
    background: var(--paper);
  }
  .canvas {
    position: relative;
    width: 1200px;
    height: 444px;
  }
  .sign {
    position: absolute;
    left: 265px;
    top: 8px;
    width: 670px;
    height: 428px;
    filter: drop-shadow(0 4px 6px rgba(0,0,0,0.25));
  }
  .headline {
    font-family: "Yesteryear", cursive;
    font-size: 128px;
  }
  .headline-fill { fill: var(--crimson); }
  .headline-shadow { fill: var(--crimson-deep); }
  .headline-highlight { fill: var(--gold-light); }
  .brand-name {
    font-family: "Barlow", sans-serif;
    font-weight: 700;
    font-size: 54px;
    fill: var(--ink);
    letter-spacing: 1px;
  }
  .brand-sub {
    font-family: "Barlow", sans-serif;
    font-weight: 700;
    font-size: 23px;
    fill: var(--ink);
  }
  .phone {
    font-family: "Barlow Condensed", sans-serif;
    font-weight: 700;
    font-size: 72px;
    fill: url(#phoneGold);
    letter-spacing: 1px;
  }
  .appointment {
    font-family: "Barlow", sans-serif;
    font-weight: 700;
    font-size: 31px;
    fill: var(--crimson);
  }
</style>
</head>
<body>
<div class="canvas">
  <svg class="sign" viewBox="0 0 900 600" xmlns="http://www.w3.org/2000/svg">
    <defs>
      <linearGradient id="plateGold" x1="0" y1="0" x2="1" y2="0">
        <stop offset="0" stop-color="var(--gold-mid)"/>
        <stop offset="0.45" stop-color="var(--gold-light)"/>
        <stop offset="1" stop-color="var(--gold-mid)"/>
      </linearGradient>
      <linearGradient id="phoneGold" x1="0" y1="0" x2="0" y2="1">
        <stop offset="0" stop-color="#f6e3a6"/>
        <stop offset="1" stop-color="#c7a25a"/>
      </linearGradient>
      <linearGradient id="frameArea" x1="0" y1="0" x2="1" y2="1">
        <stop offset="0" stop-color="#e8c56a"/>
        <stop offset="1" stop-color="#b08532"/>
      </linearGradient>
      <clipPath id="faceClip">
        <path d="M14,66 L162,66 L197,24 L683,24 L718,66 L866,66 L866,330 C858,405 796,458 716,472 L664,488 L440,556 L216,488 L164,472 C84,458 22,405 14,330 Z"/>
      </clipPath>
    </defs>

    <g transform="translate(10,6)">
      <!-- sign plate -->
      <path class="plate-edge" fill="var(--crimson)"
        d="M0,42 L150,42 L185,0 L695,0 L730,42 L880,42 L880,330 C872,420 805,480 720,495 L670,512 L440,585 L210,512 L160,495 C75,480 8,420 0,330 Z"/>
      <path class="plate-band" fill="var(--gold-band)"
        d="M12,54 L156,54 L191,12 L689,12 L724,54 L868,54 L868,330 C860,412 798,466 718,482 L668,498 L440,570 L212,498 L162,482 C82,466 20,412 12,330 Z"/>
      <path class="plate-face" fill="url(#plateGold)"
        d="M14,66 L162,66 L197,24 L683,24 L718,66 L866,66 L866,330 C858,405 796,458 716,472 L664,488 L440,556 L216,488 L164,472 C84,458 22,405 14,330 Z"/>

      <!-- top ornament rule -->
      <g class="rule-top" fill="var(--ink)">
        <path d="M270,45 L415,43 L415,46 Z"/>
        <path d="M610,45 L465,43 L465,46 Z"/>
        <rect x="435" y="39" width="9" height="9" transform="rotate(45 439.5 43.5)"/>
        <rect x="420" y="41" width="5" height="5" transform="rotate(45 422.5 43.5)"/>
        <rect x="455" y="41" width="5" height="5" transform="rotate(45 457.5 43.5)"/>
      </g>

      <!-- picture frame visual, kept inside the plate -->
      <g clip-path="url(#faceClip)">
        <g role="img" aria-label="Ornate gilded picture frame">
          <rect x="605" y="268" width="205" height="220" fill="url(#frameArea)"/>
          <rect x="635" y="300" width="145" height="188" fill="url(#plateGold)"/>
        </g>
        <g role="img" aria-label="Crimson flourish ornament">
          <rect x="818" y="322" width="30" height="100" rx="15" fill="var(--crimson)" opacity="0.55"/>
        </g>
      </g>

      <!-- headline -->
      <g class="headline">
        <text class="headline-shadow" x="48" y="176">Custom</text>
        <text class="headline-highlight" x="42" y="170">Custom</text>
        <text class="headline-fill" x="45" y="173">Custom</text>
        <text class="headline-shadow" x="38" y="284">Framing</text>
        <text class="headline-highlight" x="32" y="278">Framing</text>
        <text class="headline-fill" x="35" y="281">Framing</text>
      </g>
      <path class="headline-swash" fill="var(--ink)" d="M120,305 C200,292 300,290 390,292 C300,294 200,298 120,308 Z"/>

      <!-- brand block: plain square marker + name -->
      <g class="brand">
        <rect class="brand-marker" x="546" y="176" width="22" height="22" fill="var(--crimson)"/>
        <text class="brand-name" x="850" y="206" text-anchor="end">TALLPINE</text>
        <text class="brand-sub" x="850" y="238" text-anchor="end">Framing Studio</text>
      </g>

      <!-- phone banner -->
      <g class="banner">
        <path d="M130,380 L185,372 L185,440 L122,446 L150,412 Z" fill="var(--ink)"/>
        <path d="M755,380 L700,372 L700,440 L763,446 L735,412 Z" fill="var(--ink)"/>
        <rect x="180" y="345" width="525" height="90" fill="var(--ink)"/>
        <rect x="186" y="351" width="513" height="78" fill="none" stroke="var(--gold-mid)" stroke-width="1.5"/>
        <text class="phone" x="442" y="416" text-anchor="middle">(555) 014-2290</text>
      </g>

      <text class="appointment" x="440" y="480" text-anchor="middle">By Appointment</text>

      <!-- bottom ornament rule -->
      <g class="rule-bottom" fill="var(--ink)">
        <path d="M345,511 L420,509 L420,512 Z"/>
        <path d="M540,511 L462,509 L462,512 Z"/>
        <rect x="437" y="507" width="6" height="6" transform="rotate(45 440 510)"/>
        <rect x="425" y="508" width="4" height="4" transform="rotate(45 427 510)"/>
        <rect x="451" y="508" width="4" height="4" transform="rotate(45 453 510)"/>
      </g>
    </g>
  </svg>
</div>
</body>
</html>
```